Modern Billboard Ad for Criminal Defense Firm

10.5 x 36 We're looking for something to set us apart from the local competition. Looking for sleek and modern. We're a mid-sized firm in a small market city. We want to give the artist room to be creative on this one.
Thanks

Target Market(s)

Adult clients who have been charged with a crime/DWI

Industry/Entity Type

legal

Font styles to use
Serif
Sans Serif

Requirements
Must have
• Needs to have the firm name in large lettering. Law Offices of Marcus T Whitfield. “PLLC” does not have to be included. Phone number of (555) 384-1927 should be included but not the main focus.
Nice to have
• A call to action or something similar. “Don’t go it alone, call today.”, “ Arrested?”

```html
<!DOCTYPE html>
<html lang="en">
<head>
<meta charset="utf-8">
<title>Marcus T Whitfield Law Office – Billboard</title>
<link rel="stylesheet" href="https://fonts.googleapis.com/css2?family=Anton&family=Montserrat:wght@600;700&family=Archivo+Narrow:wght@400;700&family=Arimo:wght@400&display=swap">
<style>
  :root {
    --page: #f7f7f8;
    --ink: #111111;
    --sky-top: #bcdcf0;
    --sky-bottom: #f1f6fa;
    --accent: #1aa7e6;
    --accent-deep: #1590c8;
    --paper: #ffffff;
    --wood-dark: rgba(96, 62, 44, 0.78);
    --wood-soft: rgba(120, 84, 62, 0.45);
    --photo-light: #d9d9d9;
    --photo-mid: #a3a3a3;
    --photo-dark: #6a6a6a;
    --badge-blue: #2a86c4;
  }
  * { box-sizing: border-box; margin: 0; padding: 0; }
  html, body {
    width: 1040px; height: 1200px; overflow: hidden;
    background: var(--page);
  }
  .canvas { position: relative; width: 1040px; height: 1200px; }
  .billboard {
    position: absolute; left: 20px; top: 455px;
    width: 1000px; height: 290px; overflow: hidden;
    background: var(--paper);
  }
  .billboard__sky {
    position: absolute; left: 0; top: 0; width: 610px; height: 290px;
    background: linear-gradient(180deg, var(--sky-top) 0%, #dbeaf5 55%, var(--sky-bottom) 100%);
  }
  .billboard__stripe { position: absolute; left: 0; top: 0; width: 1000px; height: 60px; }
  .still-life {
    position: absolute; left: 0; top: 24px; width: 300px; height: 266px;
    background: linear-gradient(180deg,
      rgba(96, 62, 44, 0) 0%,
      var(--wood-soft) 25%,
      rgba(120, 84, 62, 0.25) 50%,
      var(--wood-dark) 68%,
      var(--wood-dark) 88%,
      rgba(220, 224, 228, 0.6) 100%);
    -webkit-mask-image: linear-gradient(90deg, #000 65%, transparent 100%);
    mask-image: linear-gradient(90deg, #000 65%, transparent 100%);
  }
  .award-badge {
    position: absolute; left: 81px; top: 159px; width: 81px; height: 118px;
    background: var(--badge-blue); border: 3px solid var(--paper);
  }
  .portrait {
    position: absolute; left: 360px; top: 20px; width: 273px; height: 270px;
    background: linear-gradient(180deg, var(--photo-light) 0%, var(--photo-mid) 55%, var(--photo-dark) 100%);
    -webkit-mask-image: linear-gradient(90deg, transparent 0%, #000 30%, #000 100%);
    mask-image: linear-gradient(90deg, transparent 0%, #000 30%, #000 100%);
  }
  .contact-band {
    position: absolute; left: 615px; top: 216px; width: 385px; height: 74px;
    background: var(--accent);
  }
  .kicker {
    position: absolute; top: 63px;
    font-family: "Montserrat", sans-serif; font-weight: 600;
    font-size: 15px; letter-spacing: 0.12em; line-height: 18px;
    color: var(--ink); white-space: nowrap;
  }
  .kicker--left { right: 569px; }
  .kicker--right { left: 622px; }
  .firm-name {
    position: absolute; top: 88px;
    font-family: "Anton", sans-serif; font-weight: 400; font-size: 66px; line-height: 1;
    color: var(--ink); white-space: nowrap;
    text-shadow: -4px 4px 0 var(--paper);
  }
  .firm-name--first { right: 583px; }
  .firm-name--last { left: 570px; }
  .firm-type {
    position: absolute; left: 681px; top: 173px;
    font-family: "Montserrat", sans-serif; font-weight: 700;
    font-size: 21px; letter-spacing: 0.38em; line-height: 26px;
    color: var(--ink); white-space: nowrap;
  }
  .contact {
    position: absolute; left: 706px; top: 240px;
    display: flex; align-items: center; gap: 6px;
    font-family: "Archivo Narrow", sans-serif; color: var(--ink); white-space: nowrap;
  }
  .contact__icon { width: 30px; height: 28px; }
  .contact__label { font-size: 21px; font-weight: 400; margin-right: 12px; }
  .contact__phone { font-size: 20px; font-weight: 700; }
  .website {
    position: absolute; left: 719px; top: 274px;
    font-family: "Arimo", sans-serif; font-size: 8.5px; letter-spacing: 0.5em;
    color: var(--ink); white-space: nowrap;
  }
</style>
</head>
<body>
<main class="canvas">
  <section class="billboard" aria-label="Marcus T Whitfield Law Office billboard">
    <div class="billboard__sky"></div>
    <svg class="billboard__stripe" viewBox="0 0 1000 60" aria-hidden="true">
      <polygon points="548,0 586,0 560,46 522,46" fill="var(--accent-deep)"/>
    </svg>
    <div class="still-life" role="img" aria-label="Photo of a wooden gavel resting on a stack of old leather-bound law books"></div>
    <div class="award-badge" role="img" aria-label="Community choice award badge"></div>
    <div class="portrait" role="img" aria-label="Black and white portrait of the attorney in a vest and tie, jacket slung over his shoulder"></div>
    <div class="contact-band"></div>

    <p class="kicker kicker--left">DON’T GO IT ALONE,</p>
    <p class="kicker kicker--right">CALL TODAY, ARRESTED?</p>
    <h1 class="firm-name firm-name--first">MARCUS T</h1>
    <h1 class="firm-name firm-name--last">WHITFIELD</h1>
    <p class="firm-type">LAW OFFICE</p>

    <div class="contact">
      <svg class="contact__icon" viewBox="0 0 30 28" aria-hidden="true">
        <path d="M9 4 C4 8 3 16 7 23 L11 20 C9 16 9 12 11 9 Z" fill="var(--ink)"/>
        <path d="M9 4 C14 2 22 2 28 6 L25 10 C20 7 15 7 11 9 Z" fill="var(--ink)"/>
      </svg>
      <span class="contact__label">CALL US</span>
      <span class="contact__phone">(555) 384-1927</span>
    </div>
    <p class="website">WWW.MWHITFIELDFIRM.COM</p>
  </section>
</main>
</body>
</html>
```